A-Stand Directional Sign Design

Objective:
We need a professional graphic design for an A-Stand sign that will guide customers arriving in our parking lot to our office. The design should be visually clear, welcoming, and aligned with our brand identity.
REQUIREMENTS:
Two versions of the design:
- One with an arrow pointing left
- One with an arrow pointing right
(This allows us to place the A-Stand anywhere and flip the graphic as needed.)
DIMENSIONS:
- Viewable Area: 30" x 40"
BRAND ALIGNMENT:
- Colors, fonts, and overall style should match our website: www.glidecrest.com
- Clean, modern, and professional look consistent with our aviation/tourism brand
CONTENT:
- Clear directional arrow (left or right depending on version)
- Text: “Office Entrance” or similar concise wording (designers may propose alternatives if they improve clarity)
READABILITY:
- Bold, high-contrast design for visibility from a distance
- Simple layout that avoids clutter
DELIVERABLES:
- Final artwork in print-ready format (PDF preferred)
- Two versions: Arrow Left and Arrow Right
DESIGN GOAL:
Ensure customers can easily find our office upon arrival, while reinforcing glideCREST’s professional and welcoming brand image.
Target Market(s)
Tourism
Look and feel

```html
<!DOCTYPE html>
<html lang="en">
<head>
<meta charset="utf-8">
<title>glideCREST Entrance A-Stand Signs</title>
<link href="https://fonts.googleapis.com/css2?family=Montserrat:wght@700;800;900&display=swap" rel="stylesheet">
<style>
  :root {
    --backdrop: #c4c4c4;
    --paper: #ffffff;
    --brand-blue: #2a7aba;
    --sky-blue: #84a9d3;
    --pale-blue: #a0bde3;
    --deep-blue: #4f7bbd;
    --night: #272c34;
    --white: #ffffff;
  }
  * { margin: 0; padding: 0; box-sizing: border-box; }
  html, body {
    width: 1200px;
    height: 825px;
    overflow: hidden;
    background: var(--backdrop);
    font-family: "Montserrat", sans-serif;
  }
  .sign {
    position: absolute;
    top: 78px;
    width: 502px;
    height: 669px;
    background: var(--paper);
    overflow: hidden;
  }
  .sign--left { left: 70px; }
  .sign--right { left: 628px; }
  .sign__art {
    position: absolute;
    inset: 0;
    width: 502px;
    height: 669px;
  }
  .sign__brand {
    position: absolute;
    top: 92px;
    left: 0;
    width: 100%;
    text-align: center;
    font-weight: 800;
    font-size: 56px;
    letter-spacing: 1px;
    color: var(--brand-blue);
    line-height: 1;
  }
  .sign__tagline {
    position: absolute;
    top: 236px;
    left: 0;
    width: 100%;
    text-align: center;
    font-weight: 800;
    font-size: 25px;
    letter-spacing: 0.5px;
    color: var(--brand-blue);
    line-height: 1;
  }
  .sign__message {
    position: absolute;
    left: 0;
    width: 100%;
    text-align: center;
    font-weight: 900;
    line-height: 1;
  }
  .sign__message--come { top: 345px; font-size: 49px; color: var(--sky-blue); }
  .sign__message--fly { top: 398px; font-size: 48px; color: var(--sky-blue); }
  .sign__message--entrance { top: 455px; font-size: 58px; color: var(--white); }
</style>
</head>
<body>

<section class="sign sign--left" aria-label="Entrance sign, arrows pointing left">
  <svg class="sign__art" viewBox="0 0 502 669" aria-hidden="true">
    <path d="M0 352 Q251 229 502 352 L502 669 L0 669 Z" fill="var(--brand-blue)"/>
    <path d="M0 368 Q251 245 502 368 L502 669 L0 669 Z" fill="var(--night)"/>
    <g fill="none" stroke-width="24" stroke-linecap="round" stroke-linejoin="round">
      <polyline points="181,545 134,584 181,624" stroke="var(--white)"/>
      <polyline points="271,545 226,584 271,624" stroke="var(--pale-blue)"/>
      <polyline points="369,545 325,584 369,624" stroke="var(--deep-blue)"/>
    </g>
  </svg>
  <div class="sign__brand">glideCREST</div>
  <div class="sign__tagline">WE CREATE MEMORIES</div>
  <div class="sign__message sign__message--come">COME</div>
  <div class="sign__message sign__message--fly">FLY WITH US</div>
  <div class="sign__message sign__message--entrance">ENTRANCE</div>
</section>

<section class="sign sign--right" aria-label="Entrance sign, arrows pointing right">
  <svg class="sign__art" viewBox="0 0 502 669" aria-hidden="true">
    <path d="M0 352 Q251 229 502 352 L502 669 L0 669 Z" fill="var(--brand-blue)"/>
    <path d="M0 368 Q251 245 502 368 L502 669 L0 669 Z" fill="var(--night)"/>
    <g fill="none" stroke-width="24" stroke-linecap="round" stroke-linejoin="round" transform="translate(502 0) scale(-1 1)">
      <polyline points="181,545 134,584 181,624" stroke="var(--white)"/>
      <polyline points="271,545 226,584 271,624" stroke="var(--pale-blue)"/>
      <polyline points="369,545 325,584 369,624" stroke="var(--deep-blue)"/>
    </g>
  </svg>
  <div class="sign__brand">glideCREST</div>
  <div class="sign__tagline">WE CREATE MEMORIES</div>
  <div class="sign__message sign__message--come">COME</div>
  <div class="sign__message sign__message--fly">FLY WITH US</div>
  <div class="sign__message sign__message--entrance">ENTRANCE</div>
</section>

</body>
</html>
```